California, rapidly growing Insurance Agency needs logo and letterhead design

we need a logo design and letterhead for an insurance company that specialize in providing businesses with insurance (workers comp , group health insurance, business insurance). I would like to see designs with a professional layout that use dark rich blues, and maybe some lighter blues mixed in. Also open to using grey and red tones. The design should communicate professional, yet current day feel (not too old/stuff or boring feel).
Updates

The company name is “Dovrel Insurance Services” If possible , would like to see a letterhead option with tag line worked in somewhere as “insurance specialist for over 45 years” Thank you!!!!

Target Market(s)

We insure businesses, do would like professional look with out being too stuffy or boring

Industry/Entity Type

Insurance Agency

Logo Text

Maybe “We make Insurance easy”

Font styles to use
Serif

Colors
3176b5
0993cd
f04b51

Requirements
Nice to have
• Would like to have rich dark blues and light mixed or also open to grey and
• Red color scheme
Should not have
• We target higher end clients, so would like to stay away from
• Any type of anime graphic

```html
<!DOCTYPE html>
<html lang="en">
<head>
<meta charset="utf-8">
<title>Dovrel Insurance Services Letterhead</title>
<link href="https://fonts.googleapis.com/css2?family=Open+Sans:wght@400;600;700&family=Roboto+Condensed:wght@700&display=swap" rel="stylesheet">
<style>
  :root {
    --red: #f04b51;
    --ink: #444446;
    --ink-dark: #2e2e30;
    --bar: #666666;
    --paper: #ffffff;
  }
  * { margin: 0; padding: 0; box-sizing: border-box; }
  html, body { width: 1040px; height: 1200px; overflow: hidden; background: var(--paper); }
  .letterhead {
    position: relative;
    width: 1040px;
    height: 1200px;
    background: var(--paper);
    font-family: "Open Sans", Arial, sans-serif;
    color: var(--ink);
  }
  .side-bar {
    position: absolute; left: 0; top: 0; width: 18px; height: 1200px;
    background: var(--bar);
  }
  .brand {
    position: absolute; top: 40px; left: 0; width: 1040px;
    display: flex; justify-content: center; align-items: center; gap: 16px;
  }
  .brand-square {
    width: 68px; height: 62px; border: 5px solid var(--bar);
  }
  .brand-name {
    font-family: "Open Sans", Arial, sans-serif;
    font-weight: 400; font-size: 30px; letter-spacing: 3px;
    color: var(--red); text-transform: uppercase; line-height: 1;
  }
  .tagline {
    position: absolute; top: 120px; left: 0; width: 1040px; text-align: center;
    font-family: "Roboto Condensed", Arial, sans-serif; font-weight: 700;
    font-size: 18px; letter-spacing: 0.6px; color: var(--ink-dark);
  }
  .letter-body {
    position: absolute; left: 100px; top: 230px; width: 842px;
    font-size: 16.5px; line-height: 20px;
  }
  .recipient { margin-top: 16px; line-height: 19px; }
  .salutation { margin-top: 47px; }
  .paragraph {
    margin-top: 27px; line-height: 27px;
    text-align: justify; hyphens: auto; -webkit-hyphens: auto;
  }
  .salutation + .paragraph { margin-top: 28px; }
  .closing { margin-top: 57px; }
  .signer-name { margin-top: 58px; font-size: 19px; font-weight: 600; color: var(--ink-dark); }
  .signer-title { margin-top: 4px; }
  .footer-band {
    position: absolute; left: 0; top: 1099px; width: 1040px; height: 101px;
  }
  .footer-contact {
    position: absolute; left: 61px; top: 1122px; width: 903px;
    text-align: center; color: #fff; font-size: 18px; white-space: nowrap;
    padding-bottom: 6px; border-bottom: 1.5px solid #fff;
  }
  .footer-contact strong { font-weight: 700; }
  .footer-address {
    position: absolute; left: 0; top: 1160px; width: 1040px;
    text-align: center; color: #fff; font-size: 18px;
  }
</style>
</head>
<body>
<main class="letterhead">
  <div class="side-bar"></div>

  <header>
    <div class="brand">
      <div class="brand-square"></div>
      <div class="brand-name">Dovrel Insurance Services</div>
    </div>
    <p class="tagline">INSURANCE SPECIALIST FOR OVER 45 YEARS</p>
  </header>

  <section class="letter-body">
    <p class="issue-date">Issuing Date: May 5, 2018</p>
    <p class="recipient">Name Of Employee Mr. XYZABC<br>Address of Employee<br>Address Line 2 etc..</p>
    <p class="salutation">Dear Mr.XYZABC</p>
    <p class="paragraph">Lorem Ipsum has been the industry's standard dummy text ever since the 1500s, when an unknown printer took a galley of type and scrambled it to make a type specimen book. It has survived not only five centuries, but also the leap into electronic typesetting, remaining essentially unchanged. It was popularised in the 1960s with the release of Tessark sheets containing Lorem Ipsum passages, and more recently with desktop publishing software like Quillset Composer including versions of Lorem Ipsum.</p>
    <p class="paragraph">Lorem Ipsum is simply dummy text of the printing and typesetting industry. Lorem Ipsum has been the industry's standard dummy text ever since the 1500s, when an unknown printer took a galley of type and scrambled it to make a type specimen book.</p>
    <p class="paragraph">It has survived not only five centuries, but also the leap into electronic typesetting, remaining essentially unchanged. It was popularised in the 1960s with the release of Tessark sheets containing Lorem IpsumIpsum passages.</p>
    <p class="closing">Yours Sincerely</p>
    <p class="signer-name">Marcus Ellery</p>
    <p class="signer-title">Managing Director</p>
  </section>

  <footer>
    <svg class="footer-band" viewBox="0 1099 1040 101" width="1040" height="101" aria-hidden="true">
      <polygon points="111,1099 1040,1099 1040,1200 87,1200 26,1150" fill="var(--red)"/>
    </svg>
    <p class="footer-contact"><strong>P:</strong> 044-987 654 321 | <strong>M:</strong> 044-987 654 321 | <strong>E:</strong> info@dovrelins.com | <strong>www.dovrelins.com</strong></p>
    <p class="footer-address">12345, Address Goes Here Country Name, 123456</p>
  </footer>
</main>
</body>
</html>
```